We need a flyer for a mail action to attract people's attention and to get new items for sale. We would like to focus on a kind of full service package, where a complete package should be advertised from a single source. Clearing out, sale guarantee, increase in value through renovation when accessing own craftsmen, home staging, etc. The flyer should be as possible to point out the benefits for the customer to have to take care of yourself. The design should be simple, elegant, yet down-to-earth and match the design and colors of the existing logo. The slogan "We Love Real Estate" should be incorporated as much as possible

please in German

We need the flyer in German please

```html
<!DOCTYPE html>
<html lang="de">
<head>
<meta charset="utf-8">
<title>AVEN – We Love Real Estate</title>
<link rel="stylesheet" href="https://fonts.googleapis.com/css2?family=Roboto:wght@500;700&display=swap">
<style>
  :root {
    --sky-deep: #0b5f9a;
    --sky-light: #bfe4f7;
    --roof-white: #ffffff;
    --brand-navy: #27226e;
    --slogan-blue: #19598a;
    --tick-green: #6dbb4a;
    --footer-navy: #11142e;
    --rule: rgba(255,255,255,0.45);
    --gold: #c9a24a;
    --gold-light: #f3dfa6;
  }
  * { margin: 0; padding: 0; box-sizing: border-box; }
  html, body { width: 927px; height: 1200px; overflow: hidden; background: #fff; }
  .flyer {
    position: relative; width: 927px; height: 1200px; overflow: hidden;
    font-family: "Roboto", Arial, sans-serif; color: #fff;
  }
  .backdrop { position: absolute; inset: 0; }
  .brand {
    position: absolute; top: 336px; left: 0; width: 100%; text-align: center;
    font-weight: 700; font-size: 84px; letter-spacing: 10px; color: var(--brand-navy); line-height: 1;
  }
  .slogan {
    position: absolute; top: 436px; left: 0; width: 100%; text-align: center;
    font-weight: 500; font-size: 35px; color: var(--slogan-blue); letter-spacing: 0.5px;
  }
  .offer {
    position: absolute; top: 592px; left: 60px; width: 532px; text-align: right;
  }
  .headline {
    font-weight: 500; font-size: 44px; letter-spacing: 0.5px; line-height: 1;
  }
  .subline {
    margin-top: 22px; font-weight: 500; font-size: 30px; line-height: 1;
  }
  .sale-badge { position: absolute; left: 636px; top: 530px; width: 208px; height: 208px; }
  .service-art {
    position: absolute; left: 48px; top: 744px; width: 450px; height: 366px;
    border-radius: 40px;
    background: radial-gradient(ellipse at 50% 45%, rgba(255,255,255,0.45), rgba(255,255,255,0.1) 70%);
  }
  .benefits { position: absolute; left: 516px; top: 768px; width: 392px; list-style: none; }
  .benefits li {
    position: relative; padding: 10px 0 12px 40px;
    font-weight: 500; font-size: 26px; line-height: 32px;
    border-bottom: 1px solid var(--rule);
  }
  .benefits li:last-child { border-bottom: none; }
  .benefits svg { position: absolute; left: 0; top: 10px; width: 32px; height: 28px; }
  .footer-rule { position: absolute; left: 0; top: 1110px; width: 100%; height: 10px; background: var(--tick-green); }
  .footer {
    position: absolute; left: 0; top: 1120px; width: 100%; height: 80px; background: var(--footer-navy);
    display: flex; align-items: center; justify-content: center; gap: 28px;
    font-size: 21px; font-weight: 500; letter-spacing: 0.3px; color: #f1f1f1;
  }
  .footer .sep { opacity: 0.8; }
</style>
</head>
<body>
<div class="flyer">
  <svg class="backdrop" width="927" height="1200" viewBox="0 0 927 1200">
    <defs>
      <linearGradient id="sky" x1="0" y1="0" x2="0" y2="1">
        <stop offset="0" stop-color="#0a5d97"/>
        <stop offset="0.5" stop-color="#4aa6d8"/>
        <stop offset="1" stop-color="#1a78b4"/>
      </linearGradient>
      <radialGradient id="glow" cx="0.5" cy="0.45" r="0.6">
        <stop offset="0" stop-color="#ffffff" stop-opacity="0.95"/>
        <stop offset="0.5" stop-color="#bfe4f7" stop-opacity="0.6"/>
        <stop offset="1" stop-color="#ffffff" stop-opacity="0"/>
      </radialGradient>
      <linearGradient id="roofFill" gradientUnits="userSpaceOnUse" x1="0" y1="244" x2="0" y2="1200">
        <stop offset="0" stop-color="#ffffff"/>
        <stop offset="0.15" stop-color="#eef0f4"/>
        <stop offset="0.25" stop-color="#b9c6da"/>
        <stop offset="0.33" stop-color="#5a88b6"/>
        <stop offset="0.41" stop-color="#1f6399"/>
        <stop offset="1" stop-color="#0d5184"/>
      </linearGradient>
    </defs>
    <rect width="927" height="480" fill="url(#sky)"/>
    <ellipse cx="463" cy="175" rx="520" ry="70" fill="url(#glow)"/>
    <polygon points="0,456 480,218 927,440 927,1200 0,1200" fill="var(--roof-white)"/>
    <polygon points="0,486 480,244 927,466 927,1200 0,1200" fill="url(#roofFill)"/>
  </svg>

  <div class="brand">AVEN</div>
  <div class="slogan">WE LOVE REAL ESTATE</div>

  <div class="offer">
    <div class="headline">RUNDUM-SORGLOS-PAKET</div>
    <div class="subline">ALLES AUS EINER HAND</div>
  </div>

  <svg class="sale-badge" viewBox="0 0 208 208" role="img" aria-label="Goldenes Angebotssiegel mit Lorbeerkranz und Bestpreis-Band">
    <defs>
      <radialGradient id="gold" cx="0.4" cy="0.35" r="0.7">
        <stop offset="0" stop-color="#f3dfa6"/>
        <stop offset="1" stop-color="#c9a24a"/>
      </radialGradient>
    </defs>
    <circle cx="104" cy="104" r="100" fill="#ffffff"/>
    <circle cx="104" cy="104" r="92" fill="url(#gold)"/>
  </svg>

  <div class="service-art" role="img" aria-label="Illustration: Hände halten ein Tablet mit Immobilienangeboten, umgeben von Symbolen für Garage, Kartensuche, Pool, Finanzierung und Verkauf"></div>

  <ul class="benefits">
    <li><svg viewBox="0 0 32 28"><path d="M2 15 L11 25 L30 3" fill="none" stroke="var(--tick-green)" stroke-width="6" stroke-linejoin="round"/></svg>Entrümpelung</li>
    <li><svg viewBox="0 0 32 28"><path d="M2 15 L11 25 L30 3" fill="none" stroke="var(--tick-green)" stroke-width="6" stroke-linejoin="round"/></svg>Verkaufsgarantie</li>
    <li><svg viewBox="0 0 32 28"><path d="M2 15 L11 25 L30 3" fill="none" stroke="var(--tick-green)" stroke-width="6" stroke-linejoin="round"/></svg>Wertsteigerung durch Renovierung mit eigenen Handwerkern</li>
    <li><svg viewBox="0 0 32 28"><path d="M2 15 L11 25 L30 3" fill="none" stroke="var(--tick-green)" stroke-width="6" stroke-linejoin="round"/></svg>Home Staging</li>
  </ul>

  <div class="footer-rule"></div>
  <footer class="footer">
    <span>555 014 2290</span><span class="sep">|</span>
    <span>KONTAKT@AVEN-IMMO.DE</span><span class="sep">|</span>
    <span>WWW.AVEN-IMMO.DE</span>
  </footer>
</div>
</body>
</html>
```